依頼詳細
既存のサイトを見ていただければ分かりやすいかと思いますが、

サロンのイメージカラーは、ブラウン+ゴールド、サロンのモチーフは白雪姫としており、リンゴとティアラを前面に出しています。

サロン名のソレッタ(Soletta)はイタリア語です。

見出しなどに使用する字体全ては、ロゴにあわせてください。

色味はブラウン+ゴールドに、薄めのピンク系、またはオレンジ系の組み合わせで、ゴールドの光沢度は、各デザイナー様にお任せいたします。

暖かい雰囲気で、高級感を前面に出しつつ、近寄りがたい雰囲気になり過ぎないデザインが希望です。

ゴシックより、明朝タイプ、角より、丸みがあるイメージを希望します。

幅広い年代から見られるので、タイトル部分などは、年配の方が見やすいよう、英語を小さめにしてカタカナ優勢でお願いします。

キラキラは必要ありませんが、まつ毛エクステに、ラメやラインストーンを使うことがあるので、ラインストーン、ラメがイメージ出来るものをデザインに組み込んでいただければ、想像しているイメージに近くなります。
サイトURL
http://www.eye-soletta-demo.com/
ページ数
2ページ
希望イメージ
シンプル 複雑
単色 カラフル
暗い 明るい
日常 高級
遊び心 厳粛
未来的 伝統的
女性的 男性的
希望する色
ブラウン+ゴールドに、薄めのピンク系、またはオレンジ系
納品ファイル
• 高解像度JPG (.jpg)
• イラストレーター形式 (.ai)
• フォトショップ形式 (.psd)
補足説明
申し訳ありません。

PDFに間違いがありましたので、新たに添付しました。
資料にある納品物に関して、psd、aiとありますが、双方納品ではなく、どちらかの形式で問題ございません。
■ 選んだ理由

ご提案をいただいたデザインは全てすばらしく、サロン様も長い時間迷っていましたが、

迷いに迷った末、こちらの提案を選ばせていただきました。

この提案はこちらの指定した色合いにとらわれず、

あえて全く違う色を使った提案になっていたのですが、

ソレッタの「幅広い年代層」から考えていただいた、

見やすさ、

さらに言うと

ユーザビリティを重視した、デザインと色使いにとても満足していらっしゃいました。

■ 提案者全員のお礼・コメント

ご提案いただきましたデザインは、当選したデザイン以外は、どれも、こちらの指定どおり忠実に考えていただき、非常に満足いくものでした。

サロン様も、どれもイメージに近かったので本当に迷ったと、おっしゃっていましたが、1つだけ異色のデザインが目につき心に残ったようです。

ご提案していただきました皆様、この度は本当にありがとうございました。

またご縁がありましたらよろしくお願い致します。

```html
<!DOCTYPE html>
<html lang="ja">
<head>
<meta charset="utf-8">
<title>eye Beautysalon Soletta</title>
<link rel="stylesheet" href="https://fonts.googleapis.com/css2?family=Shippori+Mincho:wght@500;700&family=Noto+Sans+JP:wght@400&display=swap">
<style>
:root{
  --gold:#c7a055;
  --gold-deep:#a8802f;
  --brown:#4a3520;
  --pink-soft:#fbeef0;
  --pink-line:#efc6cc;
  --cream:#fdf9ef;
  --frame:#c9ab74;
  --ink:#2f2f2f;
  --muted:#9a9a9a;
}
*{margin:0;padding:0;box-sizing:border-box}
html,body{width:1200px;height:4644px;overflow:hidden;background:#fff}
.page{position:relative;width:1200px;height:4644px;background:#fff;font-family:"Shippori Mincho",serif}
.rose-deco{position:absolute;left:640px;top:1080px;width:560px;height:1500px;
  background:radial-gradient(ellipse at 60% 30%,rgba(239,198,204,.35),rgba(255,255,255,0) 65%)}
.brand{position:absolute;left:60px;top:90px;display:flex;align-items:center;gap:28px}
.brand-mark{width:40px;height:40px;border-radius:50%;background:var(--gold)}
.brand-name{font-size:170px;font-weight:500;color:var(--gold);line-height:1}
.brand-sub{position:absolute;left:760px;top:250px;font-family:"Noto Sans JP",sans-serif;font-size:46px;color:var(--gold-deep)}
.slider{position:absolute;left:32px;top:452px;width:1136px;height:608px;background:var(--cream);border:3px solid var(--frame)}
.slider-text{position:absolute;inset:0;display:flex;flex-direction:column;justify-content:center;align-items:center;
  font-family:"Noto Sans JP",sans-serif;font-weight:400;font-size:36px;line-height:72px;color:var(--brown);font-weight:700}
.slider-arrow{position:absolute;top:235px;font-size:120px;line-height:1;color:var(--gold-deep);font-family:"Shippori Mincho",serif}
.slider-arrow.prev{left:-10px}
.slider-arrow.next{right:-10px}
.main-nav{position:absolute;left:0;top:1092px;width:1200px;list-style:none;text-align:center}
.main-nav li{font-size:50px;line-height:112px;color:var(--gold)}
.divider{position:absolute;left:240px;width:720px;height:20px}
.cta{position:absolute;left:0;width:1200px;text-align:center;font-size:56px;color:var(--gold)}
.map{position:absolute;left:32px;top:2632px;width:1136px;height:760px;background:linear-gradient(160deg,#eeebe4,#e2ddd3)}
.lace-band{position:absolute;left:0;top:3420px;width:1200px;height:60px;background:linear-gradient(var(--pink-soft),var(--pink-line))}
.shop-info{position:absolute;left:80px;top:3500px;font-family:"Noto Sans JP",sans-serif;font-size:46px;line-height:64px;color:var(--ink)}
.shop-info p{margin-bottom:64px}
.credit{display:flex;align-items:center;gap:40px}
.cards{display:flex;gap:22px}
.card{width:100px;height:64px;border-radius:6px}
.footer{position:absolute;left:0;top:4556px;width:1200px;height:88px;background:var(--pink-soft);border-top:6px solid var(--pink-line);
  display:flex;align-items:center;justify-content:center;font-family:"Noto Sans JP",sans-serif;font-size:28px;color:var(--muted);letter-spacing:1px}
</style>
</head>
<body>
<div class="page">
  <div class="rose-deco" role="img" aria-label="淡いピンクのバラの線画の装飾"></div>

  <header>
    <div class="brand"><span class="brand-mark"></span><span class="brand-name">Soletta</span></div>
    <div class="brand-sub">eye Beautysalon</div>
  </header>

  <section class="slider">
    <span class="slider-arrow prev">&lt;</span>
    <div class="slider-text">
      <span>学割、初回半額、</span>
      <span>ブライダルのキャンペーンを</span>
      <span>Ajaxで切り替え</span>
    </div>
    <span class="slider-arrow next">&gt;</span>
  </section>

  <ul class="main-nav">
    <li>HOME</li>
    <li>メニュー</li>
    <li>ソレッタのまつげデザイン</li>
    <li>施術の流れ</li>
    <li>お客様の声</li>
    <li>Q&amp;A</li>
    <li>キャンペーン</li>
  </ul>

  <svg class="divider" style="top:2110px" viewBox="0 0 720 20"><line x1="0" y1="10" x2="720" y2="10" stroke="#efc6cc" stroke-width="3"/><path d="M360 0 L372 10 L360 20 L348 10Z" fill="#efc6cc"/></svg>
  <div class="cta" style="top:2200px">今すぐネット予約をする</div>
  <svg class="divider" style="top:2352px" viewBox="0 0 720 20"><line x1="0" y1="10" x2="720" y2="10" stroke="#efc6cc" stroke-width="3"/><path d="M360 0 L372 10 L360 20 L348 10Z" fill="#efc6cc"/></svg>
  <div class="cta" style="top:2432px">今すぐTEL予約をする</div>

  <div class="map" role="img" aria-label="サロン周辺の地図"></div>
  <div class="lace-band" role="img" aria-label="ピンクのレース模様の帯"></div>

  <section class="shop-info">
    <p>227-0091<br>横浜市緑区さくら台3-8-1 2階<br>花村ビル ガーデンショップ</p>
    <p>アクセス<br>みどり線　さくら台駅下車　徒歩１分</p>
    <p>営業時間<br>10:00～19:00(最終受付18:30)</p>
    <p>定休日　　日曜日</p>
    <p>ご予約おといあわせ<br>045-000-1234</p>
    <div class="credit">
      <span>取扱クレジット</span>
      <div class="cards">
        <span class="card" style="background:#2a3f8f"></span>
        <span class="card" style="background:#d8492c"></span>
        <span class="card" style="background:#2f7a3c"></span>
        <span class="card" style="background:#3a8cc4"></span>
        <span class="card" style="background:#dfe3ea;border:2px solid #9aa6b8"></span>
      </div>
    </div>
  </section>

  <footer class="footer">Copyright (c)2012 eye Beautysalon Soletta All Rights Reserved.</footer>
</div>
</body>
</html>
```